Webdesign für Fahrschule
Sehr ansprechendes, modernes und übersichtliches Design, welches das Unternehmen sehr gut widerspiegelt
Zielgruppe
Fahrschule mit fach- und sachgerechter Fahrschulausbildung in allen Zweiradklassen und im PKW-Bereich sowie Ausbildung auf Automatikfahrzeugen und Führerscheinausbildung für Behinderte
Aufgabenstellung
Keine Kopie der alten Seite
Nutzerfreundliche Unternehmenswebseite
Design soll frisch, modern und aussagekräftig erscheinen

```html
<!DOCTYPE html>
<html lang="de">
<head>
<meta charset="utf-8">
<title>Fahrschule Hartwig</title>
<link href="https://fonts.googleapis.com/css2?family=Lato:wght@400;700&family=Poppins:wght@400;500;600&display=swap" rel="stylesheet">
<style>
:root{
  --green:#00b21b;
  --green-dark:#009a17;
  --ink:#1d1d1d;
  --muted:#5a5a5a;
  --soft:#f3f3f3;
  --line:#e4e4e4;
  --yellow:#fff200;
}
*{margin:0;padding:0;box-sizing:border-box}
html,body{width:1054px;height:1200px;overflow:hidden;background:#fff}
body{position:relative;font-family:'Lato',sans-serif;color:var(--ink)}
.abs{position:absolute}

.corner-deco{left:0;top:0;width:52px;height:103px;background:linear-gradient(135deg,var(--green) 0%,#6fd97c 100%)}

.brand{left:126px;top:36px;width:180px;display:flex;align-items:center;gap:7px;font-family:'Poppins',sans-serif;font-weight:600;font-size:14px;color:var(--green);white-space:nowrap}
.brand-dot{width:30px;height:30px;border-radius:50%;background:var(--ink);flex:none}
.nav{left:323px;top:42px;display:flex;gap:18px;font-family:'Poppins',sans-serif;font-weight:500;font-size:12px}
.nav a{color:var(--ink);text-decoration:none}
.nav a.active{color:var(--green)}
.call-btn{left:775px;top:38px;width:153px;height:30px;background:var(--green);color:#fff;display:flex;align-items:center;justify-content:center;gap:7px;font-family:'Poppins',sans-serif;font-size:14px;border-radius:2px}

.hero-ring{left:799px;top:157px}
.hero-title{left:126px;top:127px;font-weight:700;font-size:51px;line-height:49px;color:var(--green);letter-spacing:-0.3px}
.hero-sub{left:126px;top:285px;width:350px;font-size:14px;line-height:22px;color:var(--muted)}
.hero-photo{left:499px;top:107px;width:428px;height:285px;background:linear-gradient(120deg,#c9b79a 0%,#6f7683 45%,#8a5a34 80%,#3d3a38 100%)}
.hero-card{left:409px;top:343px;width:316px;height:80px;background:#fff;box-shadow:0 4px 12px rgba(0,0,0,.15);display:flex;align-items:center;justify-content:center;font-size:14px}

.welcome{left:0;top:499px;width:1054px;height:372px;background:var(--soft)}
.welcome-kicker{left:126px;top:540px;font-family:'Poppins',sans-serif;font-weight:500;font-size:13px}
.welcome-title{left:126px;top:556px;font-family:'Poppins',sans-serif;font-weight:600;font-size:40px;line-height:39px;color:var(--green)}
.photo-a{left:128px;top:672px;width:231px;height:154px;background:linear-gradient(110deg,#2f4a6c 0%,#7c8896 50%,#3a4f68 100%)}
.photo-b{left:370px;top:673px;width:92px;height:153px;background:linear-gradient(160deg,#7d9463 0%,#b9b3ad 45%,#2a2a2a 100%)}
.welcome-text{left:490px;top:538px;width:435px;font-size:11px;line-height:19px}
.welcome-text p{margin-bottom:19px}

.contact-band{left:0;top:871px;width:1054px;height:143px;background:var(--green);overflow:hidden}
.band-photo{left:560px;top:0;width:380px;height:143px;background:radial-gradient(ellipse at 60% 55%,#7ef27f 0%,#2fd23c 40%,rgba(0,178,27,0) 75%)}
.band-note{left:151px;top:904px;font-size:13.5px;color:#fff}
.band-title{left:151px;top:930px;font-weight:700;font-size:21.5px;line-height:26px;color:#fff}
.band-title span{color:var(--yellow)}

.foot-mark{left:126px;top:1042px;width:37px;height:37px;border-radius:50%;border:2px solid #777}
.foot-col{font-size:11px;line-height:19px;display:flex;gap:8px}
.foot-address{left:289px;top:1044px}
.foot-contact{left:548px;top:1044px}
.social{left:860px;top:1050px;display:flex;gap:15px}
.social span{width:12px;height:12px;border-radius:50%}
.copyright{left:126px;top:1133px;width:800px;height:43px;border:1px solid var(--line);background:#f8f8f8;display:flex;align-items:center;justify-content:center;font-size:11px}
</style>
</head>
<body>
<div class="abs corner-deco" role="img" aria-label="Grünes Dreiecksmuster"></div>

<div class="abs brand"><span class="brand-dot"></span>Fahrschule Hartwig</div>
<nav class="abs nav">
  <a class="active" href="#">Startseite</a><a href="#">Anmeldung</a><a href="#">Aufbauseminar</a><a href="#">Kontakt</a><a href="#">Impressum</a>
</nav>
<div class="abs call-btn">
  <svg width="14" height="14" viewBox="0 0 24 24" fill="none" stroke="#fff" stroke-width="2"><path d="M5 3h4l2 5-3 2a11 11 0 0 0 6 6l2-3 5 2v4a2 2 0 0 1-2 2A17 17 0 0 1 3 5a2 2 0 0 1 2-2z"/></svg>
  0170 - 555 01 23
</div>

<svg class="abs hero-ring" width="320" height="320" viewBox="0 0 320 320"><circle cx="157" cy="157" r="153" fill="none" stroke="var(--green)" stroke-width="8"/></svg>
<h1 class="abs hero-title">Fahrschule für<br>behinderte<br>Autofahrer</h1>
<p class="abs hero-sub">professionelle und bedarfsgerechte Fahrschulausbildung in allen Zweiradklassen und im PKW-Bereich.</p>
<div class="abs hero-photo" role="img" aria-label="Foto: Mann im Rollstuhl steigt in ein Auto"></div>
<div class="abs hero-card">Wir machen Ihre Mobilitätsträume wahr</div>

<section class="abs welcome"></section>
<div class="abs welcome-kicker">Herzlich Willkommen bei der</div>
<h2 class="abs welcome-title">Fahrschule<br>Hartwig!</h2>
<div class="abs photo-a" role="img" aria-label="Foto: Frau steigt vom Rollstuhl ins Auto"></div>
<div class="abs photo-b" role="img" aria-label="Foto: Fahrer in einem umgebauten Fahrzeug"></div>
<div class="abs welcome-text">
  <p>Ihr seid auf der Suche nach einer Fahrschule die euch schnell, sicher und gut ausgebildet zum Führerschein bringt?</p>
  <p>Dann seid Ihr hier genau richtig ! ! !</p>
  <p>Wir bieten euch eine fach- und sachgerechte Fahrschulausbildung in allen Zweiradklassen und natürlich im PKW-Bereich.</p>
  <p>Aber auch die Ausbildung auf Automatikfahrzeugen und die Führerscheinausbildung für Behinderte ist bei uns möglich.</p>
  <p>Für persönliche Fragen und Anmeldungen sind wir immer Montag und Donnerstag von 16:00 Uhr bis 18:00 Uhr im Büro am Lindenweg 12 in 09111 Talstadt / OT Wiesental oder in unserer Filiale in der Parkallee 9 in 09112 Talstadt (bitte nur nach Voranmeldung) zu erreichen.</p>
</div>

<section class="abs contact-band">
  <div class="abs band-photo" role="img" aria-label="Foto: Hand am Telefonhörer, grün eingefärbt"></div>
</section>
<p class="abs band-note">Andere Termine sind nach Vereinbarung selbstverständlich möglich.</p>
<p class="abs band-title">Für telefonische Fragen könnt Ihr uns unter<br><span>0170 / 5550123</span> kontaktieren.</p>

<div class="abs foot-mark"></div>
<div class="abs foot-col foot-address">
  <svg width="14" height="16" viewBox="0 0 24 24" fill="none" stroke="#666" stroke-width="2"><path d="M12 22s7-7 7-12a7 7 0 0 0-14 0c0 5 7 12 7 12z"/><circle cx="12" cy="10" r="2.5"/></svg>
  <div>Fahrschule Lukas Hartwig<br>Lindenweg 12<br>09111 Talstadt / OT Wiesental</div>
</div>
<div class="abs foot-col foot-contact">
  <div style="display:flex;flex-direction:column;gap:6px;padding-top:3px">
    <svg width="13" height="13" viewBox="0 0 24 24" fill="none" stroke="#666" stroke-width="2"><path d="M5 3h4l2 5-3 2a11 11 0 0 0 6 6l2-3 5 2v4a2 2 0 0 1-2 2A17 17 0 0 1 3 5a2 2 0 0 1 2-2z"/></svg>
    <svg width="13" height="13" viewBox="0 0 24 24" fill="none" stroke="#666" stroke-width="2"><rect x="3" y="5" width="18" height="14"/><path d="M3 6l9 7 9-7"/></svg>
  </div>
  <div>0170 / 5550123<br>info@fahrschule-hartwig.example</div>
</div>
<div class="abs social"><span style="background:#1877f2"></span><span style="background:#e4405f"></span><span style="background:#111"></span></div>

<div class="abs copyright">© 2025. talstadt-lernt-fahren.example</div>
</body>
</html>
```